Vorelin
Montclaro SAS
Vorelin - Personal Care
Modern
Lucila Barrios Quintero
Presidente
Av. Carrera 57 #18B-64 Bogota, Colombia
lucilabarriosquintero@correoplum.net
www.vorelin-demo.net
Vorelin is the brand;s name Montclaro SAS is the firm´s name We sell shampoo and hair tonic. çthey are good quality products, for elegant consumers.
One side can go Vorelin, the other side Montclaro, for instance. Vorelin is the important one, Vorelin has a logo I want the principal side of the business card with white background and blue letters. The other side blue background.

```html
<!DOCTYPE html>
<html lang="es">
<head>
<meta charset="utf-8">
<title>Vorelin – Tarjetas de presentación</title>
<link href="https://fonts.googleapis.com/css2?family=Lato:wght@400;700&display=swap" rel="stylesheet">
<style>
  :root {
    --stage: #d9d6d2;
    --white: #ffffff;
    --blue: #1d4a8a;
    --blue-soft: #3f679f;
    --on-blue: #ffffff;
    --on-blue-soft: #d3def0;
    --rule-light: #9fb3d3;
    --silver-hi: #f4f4f4;
    --silver-lo: #9a9a9a;
  }
  * { box-sizing: border-box; margin: 0; padding: 0; }
  html, body { width: 1200px; height: 852px; overflow: hidden; }
  body {
    background: var(--stage);
    font-family: "Lato", "Gill Sans", Arial, sans-serif;
    position: relative;
  }
  .card {
    position: absolute;
    width: 540px;
    height: 310px;
    border-radius: 18px;
    overflow: hidden;
    box-shadow: 0 10px 28px rgba(0,0,0,.28);
  }
  .card--front { left: 40px; top: 150px; background: var(--white); color: var(--blue); }
  .card--back { left: 620px; top: 392px; background: var(--blue); color: var(--on-blue); }
  .card__edge {
    position: absolute; left: 0; right: 0; bottom: 0; height: 24px;
    background: linear-gradient(180deg, var(--silver-hi), var(--silver-lo));
  }
  .brand {
    position: absolute;
    display: flex; align-items: center; gap: 12px;
    font-weight: 400;
    letter-spacing: 1px;
    white-space: nowrap;
  }
  .brand__dot { width: 14px; height: 14px; border-radius: 50%; background: var(--blue); }
  .card--front .brand { left: 108px; top: 56px; font-size: 54px; }
  .card--back .brand { left: 30px; top: 118px; font-size: 28px; color: var(--on-blue); }

  .holder { position: absolute; font-size: 13px; line-height: 1.4; }
  .holder__name { font-weight: 700; font-size: 14px; }
  .holder__address { margin-top: 10px; }
  .card--front .holder { left: 40px; top: 184px; width: 215px; text-align: right; }
  .card--front .holder__role,
  .card--front .holder__address { color: var(--blue-soft); }
  .card--back .holder { left: 262px; top: 50px; }
  .card--back .holder__role,
  .card--back .holder__address { color: var(--on-blue-soft); }

  .divider { position: absolute; width: 1px; }
  .card--front .divider { left: 270px; top: 178px; height: 96px; background: var(--blue-soft); }
  .card--back .divider { left: 248px; top: 50px; height: 224px; background: var(--rule-light); }

  .contacts { position: absolute; list-style: none; font-size: 12px; line-height: 19px; }
  .contacts li { display: flex; align-items: center; gap: 8px; white-space: nowrap; }
  .contacts svg { width: 11px; height: 11px; flex: none; }
  .card--front .contacts { left: 282px; top: 178px; color: var(--blue-soft); }
  .card--front .contacts svg { fill: var(--blue); }
  .card--back .contacts { left: 262px; top: 172px; color: var(--on-blue-soft); }
  .card--back .contacts svg { fill: var(--on-blue); }
</style>
</head>
<body>

<article class="card card--front">
  <div class="brand"><span class="brand__dot"></span>Vorelin</div>
  <div class="holder">
    <p class="holder__name">Lucila Barrios Quintero</p>
    <p class="holder__role">Presidente</p>
    <p class="holder__address">Av. Carrera 57 #18B-64<br>Bogota, Colombia</p>
  </div>
  <div class="divider"></div>
  <ul class="contacts">
    <li><svg viewBox="0 0 12 12"><path d="M2 1l2 0 1 3-1.3 1a7 7 0 0 0 3.3 3.3L8 7l3 1v2c0 .6-.4 1-1 1A9 9 0 0 1 1 2c0-.6.4-1 1-1z"/></svg>571-4390218</li>
    <li><svg viewBox="0 0 12 12"><path d="M3 0h6v12H3zM4 1.5v7.5h4V1.5z"/></svg>57-3157720946 / 57-3196634172</li>
    <li><svg viewBox="0 0 12 12"><path d="M3 0h6v3H3zM1 4h10v5H9v3H3V9H1zM4 8v3h4V8z"/></svg>571-4390277</li>
    <li><svg viewBox="0 0 12 12"><path d="M6 0a6 6 0 1 0 3 11.2l-.6-1A4.8 4.8 0 1 1 10.8 6v.8c0 .6-.4 1-.9 1S9 7.4 9 6.8V3.5H8V4a3 3 0 1 0 .3 3.9A2 2 0 0 0 12 6.8V6a6 6 0 0 0-6-6zm0 4.2a1.8 1.8 0 1 1 0 3.6 1.8 1.8 0 0 1 0-3.6z"/></svg>lucilabarriosquintero@correoplum.net</li>
    <li><svg viewBox="0 0 12 12"><path d="M6 0a6 6 0 1 0 0 12A6 6 0 0 0 6 0zm0 1.2c.7.8 1.2 2 1.4 3.3H4.6C4.8 3.2 5.3 2 6 1.2zM1.3 5.5h2.2c0 .9.1 1.7.3 2.5H2a4.8 4.8 0 0 1-.7-2.5zm3.3 0h2.8c0 .9-.1 1.7-.3 2.5H4.9a9 9 0 0 1-.3-2.5zm3.9 0h2.2c0 .9-.3 1.8-.7 2.5H8.2c.2-.8.3-1.6.3-2.5zM6 10.8c-.5-.5-.8-1.1-1-1.8h2c-.2.7-.5 1.3-1 1.8z"/></svg>www.vorelin-demo.net</li>
  </ul>
  <div class="card__edge"></div>
</article>

<article class="card card--back">
  <div class="brand">Montclaro SAS</div>
  <div class="divider"></div>
  <div class="holder">
    <p class="holder__name">Lucila Barrios Quintero</p>
    <p class="holder__role">Presidente</p>
    <p class="holder__address">Av. Carrera 57 #18B-64<br>Bogota, Colombia</p>
  </div>
  <ul class="contacts">
    <li><svg viewBox="0 0 12 12"><path d="M2 1l2 0 1 3-1.3 1a7 7 0 0 0 3.3 3.3L8 7l3 1v2c0 .6-.4 1-1 1A9 9 0 0 1 1 2c0-.6.4-1 1-1z"/></svg>571-4390218</li>
    <li><svg viewBox="0 0 12 12"><path d="M3 0h6v12H3zM4 1.5v7.5h4V1.5z"/></svg>57-3157720946 / 57-3196634172</li>
    <li><svg viewBox="0 0 12 12"><path d="M3 0h6v3H3zM1 4h10v5H9v3H3V9H1zM4 8v3h4V8z"/></svg>571-4390277</li>
    <li><svg viewBox="0 0 12 12"><path d="M6 0a6 6 0 1 0 3 11.2l-.6-1A4.8 4.8 0 1 1 10.8 6v.8c0 .6-.4 1-.9 1S9 7.4 9 6.8V3.5H8V4a3 3 0 1 0 .3 3.9A2 2 0 0 0 12 6.8V6a6 6 0 0 0-6-6zm0 4.2a1.8 1.8 0 1 1 0 3.6 1.8 1.8 0 0 1 0-3.6z"/></svg>lucilabarriosquintero@correoplum.net</li>
    <li><svg viewBox="0 0 12 12"><path d="M6 0a6 6 0 1 0 0 12A6 6 0 0 0 6 0zm0 1.2c.7.8 1.2 2 1.4 3.3H4.6C4.8 3.2 5.3 2 6 1.2zM1.3 5.5h2.2c0 .9.1 1.7.3 2.5H2a4.8 4.8 0 0 1-.7-2.5zm3.3 0h2.8c0 .9-.1 1.7-.3 2.5H4.9a9 9 0 0 1-.3-2.5zm3.9 0h2.2c0 .9-.3 1.8-.7 2.5H8.2c.2-.8.3-1.6.3-2.5zM6 10.8c-.5-.5-.8-1.1-1-1.8h2c-.2.7-.5 1.3-1 1.8z"/></svg>www.vorelin-demo.net</li>
  </ul>
  <div class="card__edge"></div>
</article>

</body>
</html>
```